The Harborline LLC Asset Classes

I'm looking for for two designs here to go into powerpoint and potentially as a standalone PDF. My company does wealth management.
Graphic Image #1
I break down the investment world into 4 broad categories
-Preservation
-Capital Markets
-Real Estate
-Alternatives
In each broad category, there are subcategories:
Preservation: cash, checking/savings accounts, money market accounts, CD's, and fixed annuities.
Capital Markets: Publicly traded stocks and bonds
Real Estate: single-family residence, retail, industrial, multifamily, and office
Alternatives: private equity, private credit, cryptocurrency, asset-backed loans, tax liens, oil & gas, litigation finance, and royalties
Graphic 2: Please see the bottom f page 1 of the Tidewater Slides PDF.
Just like in graphic one, you have 4 categories of the Capital Markets and their respective subcategories
Category 1: Domestic Stocks: Subcategories are Large, mid, and small size companies
Category 2: International Stocks: Subcategories are Large, Mid/Small and by region - Developed and Emerging
Category 3: Fixed Income: You have subcategories like corporate, municipal, government, domestic, international
Category 4: Alternatives: The subcategories are metals and real estate
---------------------
I'm looking to create a graphic (either pie chart, or a circle broken into parts or some other clever way to illustrate this) to clearly illustrate both of these universes in a clean, professional, slick manner.
Target Market(s)
Investors
Colors
Designer to choose colors to be used in the design.
Requirements
Must have
- Clean
- professional
- Easy to read
- Creative
- Visually appealling
Nice to have
- I have attached my logo and some marketing materials so you can get a feel of what I am doing. Maybe you can clean this up too!

```html
<!DOCTYPE html>
<html lang="en">
<head>
<meta charset="utf-8">
<title>The Harborline LLC – Asset Classes</title>
<link href="https://fonts.googleapis.com/css2?family=Inter:wght@300;400;700&display=swap" rel="stylesheet">
<style>
  :root{
    --teal:#5ec7c9;
    --teal-box:#72cbd2;
    --sky:#49c5ec;
    --azure:#45a1d8;
    --navy:#1f63a3;
    --band:#4a61ac;
    --ring:#14568c;
    --brand:#1d5f92;
    --white:#ffffff;
  }
  *{box-sizing:border-box;margin:0;padding:0}
  html,body{width:873px;height:1200px;overflow:hidden;background:#fff}
  body{font-family:"Inter",Arial,sans-serif;position:relative}
  .panel{position:absolute;left:0;width:873px;overflow:hidden}
  .panel--universe{top:0;height:613px}
  .panel--markets{top:613px;height:587px}
  .brand{position:absolute;display:flex;align-items:center;gap:10px;
    font-family:"Inter",Arial,sans-serif;font-weight:700;font-size:25px;color:var(--brand);letter-spacing:-.3px}
  .brand__dot{width:30px;height:30px;border-radius:50%;background:var(--brand)}
  .chevron{position:absolute;display:flex;align-items:center;justify-content:center;text-align:center;
    color:var(--white);font-weight:400;line-height:1.35;
    clip-path:polygon(0 0,calc(100% - 15px) 0,100% 50%,calc(100% - 15px) 100%,0 100%,15px 50%);
    padding:0 14px 0 22px}
  .tile{position:absolute;display:flex;align-items:center;justify-content:center;text-align:center;
    color:var(--white);font-weight:700;line-height:1.25;padding:0 4px}
  .tile--light{font-weight:400}
  .c1{background:var(--teal)} .t1{background:var(--teal-box)}
  .c2,.t2{background:var(--sky)}
  .c3,.t3{background:var(--azure)}
  .c4,.t4{background:var(--navy)}
  .band{position:absolute;left:0;width:873px;height:45px;background:var(--band)}
  .ring{position:absolute}
  .panel--universe .chevron{top:99px;height:64px;font-size:18.5px;width:204px}
  .panel--universe .tile{width:176px;height:41px;font-size:13.5px}
  .panel--markets .chevron{top:97px;height:68px;font-size:19.5px;width:224px}
  .panel--markets .tile{width:194px;height:43px;font-size:15px}
</style>
</head>
<body>

<section class="panel panel--universe">
  <div class="brand" style="left:598px;top:33px"><span class="brand__dot"></span>The Harborline LLC</div>

  <div class="chevron c1" style="left:22px">Preservation</div>
  <div class="chevron c2" style="left:210px">Capital<br>Markets</div>
  <div class="chevron c3" style="left:398px">Real Estate</div>
  <div class="chevron c4" style="left:586px;font-size:20px">Alternatives</div>

  <div class="tile t1" style="left:24px;top:172px">Cash</div>
  <div class="tile t1" style="left:24px;top:219px">Checking/Savings<br>accounts</div>
  <div class="tile t1" style="left:24px;top:265px">Money market<br>accounts</div>
  <div class="tile t1" style="left:24px;top:312px">CD's</div>
  <div class="tile t1" style="left:24px;top:358px">Fixed annuities</div>

  <div class="tile t2" style="left:213px;top:172px">Publicly traded stocks<br>and bonds</div>

  <div class="tile t3" style="left:400px;top:172px;font-size:12.5px">Single-family residence</div>
  <div class="tile t3" style="left:400px;top:219px">Retail</div>
  <div class="tile t3" style="left:400px;top:265px">Industrial</div>
  <div class="tile t3" style="left:400px;top:312px">Multifamily</div>
  <div class="tile t3" style="left:400px;top:358px">Office</div>

  <div class="tile t4" style="left:589px;top:172px">Private equity</div>
  <div class="tile t4" style="left:589px;top:219px">Private credit</div>
  <div class="tile t4" style="left:589px;top:265px">Cryptocurrency</div>
  <div class="tile t4" style="left:589px;top:312px">Asset-backed loans</div>
  <div class="tile t4" style="left:589px;top:358px">Tax liens</div>
  <div class="tile t4" style="left:589px;top:405px">Oil &amp; gas</div>
  <div class="tile t4" style="left:589px;top:452px">Litigation finance</div>
  <div class="tile t4" style="left:589px;top:498px">Royalties</div>

  <div class="band" style="top:568px"></div>
  <svg class="ring" style="left:773px;top:468px" width="100" height="145" viewBox="0 0 100 145">
    <circle cx="100" cy="100" r="63" fill="none" stroke="var(--ring)" stroke-width="50"/>
  </svg>
</section>

<section class="panel panel--markets">
  <div class="brand" style="left:614px;top:33px"><span class="brand__dot"></span>The Harborline LLC</div>

  <div class="chevron c1" style="left:12px">Domestic<br>Stocks</div>
  <div class="chevron c2" style="left:219px">International<br>Stocks</div>
  <div class="chevron c3" style="left:426px">Fixed Income</div>
  <div class="chevron c4" style="left:634px;font-size:21px">Alternatives</div>

  <div class="tile t1" style="left:14px;top:175px;font-size:14.5px">Large size companies</div>
  <div class="tile t1" style="left:14px;top:224px;font-size:14.5px">Mid size companies</div>
  <div class="tile t1" style="left:14px;top:272px;font-size:14.5px">Small size companies</div>

  <div class="tile t2" style="left:222px;top:175px">Large</div>
  <div class="tile t2" style="left:222px;top:224px">Mid</div>
  <div class="tile t2" style="left:222px;top:272px">Small</div>
  <div class="tile t2 tile--light" style="left:222px;top:321px">Developed regions</div>
  <div class="tile t2 tile--light" style="left:222px;top:370px">Emerging regions</div>

  <div class="tile t3" style="left:430px;top:175px">Corporate</div>
  <div class="tile t3" style="left:430px;top:224px">Municipal</div>
  <div class="tile t3" style="left:430px;top:272px">Government</div>
  <div class="tile t3" style="left:430px;top:321px">Domestic</div>
  <div class="tile t3" style="left:430px;top:370px">International</div>

  <div class="tile t4" style="left:637px;top:175px">Metals</div>
  <div class="tile t4" style="left:637px;top:224px">Estate</div>

  <div class="band" style="top:542px"></div>
  <svg class="ring" style="left:773px;top:442px" width="100" height="145" viewBox="0 0 100 145">
    <circle cx="100" cy="100" r="63" fill="none" stroke="var(--ring)" stroke-width="50"/>
  </svg>
</section>

</body>
</html>
```